Retractable Banner Design for Retail Shopping Event

I need a design for a 33” by 86” retractable banner. It should have my logo at the top (the largest element of the design) and the banner should also include my website and Instagram handle:
www.verikamode.com
@verikamode
I have included product pictures in the brief that can be used. I also included different versions of my logo file, including AI. I need the file to be ready to upload to my printer.
My store is an upscale women’s boutique. I am also attaching designs I have selected in the past to give an idea of my aesthetic.

```html
<!DOCTYPE html>
<html lang="en">
<head>
<meta charset="utf-8">
<title>Verika Mode — Our Collections Banner</title>
<link href="https://fonts.googleapis.com/css2?family=Marcellus&display=swap" rel="stylesheet">
<style>
  :root {
    --page-bg: #f4e7e4;
    --banner-pink: #efd3cd;
    --banner-mist: #efeeee;
    --logo-fill: #eed1cb;
    --ink: #5d6162;
    --gold-dark: #b8942c;
    --gold-light: #f4cd68;
    --gold-glow: rgba(226, 190, 110, 0.55);
    --tile-white: #ffffff;
    --footer-white: #ffffff;
    --footer-ink: #2f3233;
  }
  * { box-sizing: border-box; margin: 0; padding: 0; }
  html, body { width: 715px; height: 1200px; overflow: hidden; }
  body {
    background: var(--page-bg);
    font-family: "Marcellus", "Optima", serif;
    color: var(--ink);
    position: relative;
  }
  .banner {
    position: absolute;
    left: 127px; top: 0;
    width: 460px; height: 1200px;
    background: linear-gradient(180deg, var(--banner-pink) 0%, #f2e4e2 30%, var(--banner-mist) 50%, #f2e4e2 72%, var(--banner-pink) 100%);
    overflow: hidden;
  }
  .logo-box {
    position: absolute;
    left: 63px; top: 22px;
    width: 339px; height: 119px;
    background: var(--logo-fill);
    border: 2px solid var(--ink);
    display: flex; align-items: center; justify-content: center;
  }
  .logo-name {
    font-size: 54px;
    letter-spacing: 4px;
    color: var(--ink);
    margin-top: -6px;
  }
  .logo-tag {
    position: absolute;
    left: 50%; bottom: -12px;
    transform: translateX(-50%);
    background: linear-gradient(180deg, #f0dbd7, #f0dcd8);
    padding: 0 9px;
    font-size: 19px;
    letter-spacing: 3px;
    line-height: 22px;
    color: var(--ink);
  }
  .section-title {
    position: absolute;
    left: 87px; top: 164px;
    width: 287px; height: 50px;
  }
  .section-title svg { position: absolute; inset: 0; }
  .section-title h1 {
    position: absolute; inset: 0;
    display: flex; align-items: center; justify-content: center;
    font-weight: 400;
    font-size: 25px;
    letter-spacing: 0.5px;
    color: var(--ink);
    padding-top: 2px;
  }
  .collection-tile {
    position: absolute;
    left: 117px;
    width: 224px; height: 212px;
    border-radius: 10px;
    background: linear-gradient(90deg, var(--gold-glow), rgba(250,236,205,0.35) 40%, rgba(250,236,205,0.35) 60%, var(--gold-glow));
    box-shadow: 0 0 4px rgba(226,190,110,0.4);
  }
  .tile-frame {
    position: absolute;
    left: 12px; top: 11px; right: 12px; bottom: 11px;
    background: linear-gradient(135deg, var(--gold-dark), var(--gold-light) 35%, var(--gold-dark) 60%, var(--gold-light) 100%);
    padding: 5px;
  }
  .tile-inner {
    position: relative;
    width: 100%; height: 100%;
    background: var(--tile-white);
  }
  .tile-rule {
    position: absolute;
    left: 12px; right: 12px; top: 12px; bottom: 20px;
    border: 1.5px solid var(--ink);
  }
  .tile-photo {
    position: absolute;
    left: 18px; right: 18px; top: 22px; bottom: 40px;
    border-radius: 6px;
  }
  .tile-label {
    position: absolute;
    left: 50%; bottom: 8px;
    transform: translateX(-50%);
    background: var(--tile-white);
    padding: 0 3px;
    font-size: 25px;
    line-height: 26px;
    color: var(--ink);
    white-space: nowrap;
  }
  .photo-jewelry { background: radial-gradient(ellipse at center, #e8c46a 0%, #f3e2b4 45%, #ffffff 75%); }
  .photo-home { background: radial-gradient(ellipse at center, #d9b979 0%, #a88a55 40%, #efe6d6 70%, #ffffff 85%); }
  .photo-sleep { background: radial-gradient(ellipse at center, #e9d2c8 0%, #b7a5b8 45%, #f3eef2 72%, #ffffff 88%); }
  .photo-accessories { background: linear-gradient(180deg, #ffffff 0%, #e6cfc3 30%, #d9bcaf 70%, #ffffff 100%); }
  .footer {
    position: absolute;
    left: 0; bottom: 0;
    width: 460px; height: 40px;
    background: var(--footer-white);
    display: flex; align-items: center; justify-content: space-between;
    padding: 0 16px 0 14px;
    font-size: 19px;
    color: var(--footer-ink);
  }
  .footer-item { display: flex; align-items: center; gap: 5px; }
  .footer-item svg { flex: none; }
  .social-dot {
    width: 15px; height: 15px;
    border-radius: 50%;
    background: var(--footer-ink);
  }
</style>
</head>
<body>
  <main class="banner">
    <header class="logo-box">
      <span class="logo-name">VERIKA</span>
      <span class="logo-tag">MODE</span>
    </header>

    <div class="section-title">
      <svg width="287" height="50" viewBox="0 0 287 50" aria-hidden="true">
        <g stroke="#5d6162" stroke-width="1.5" fill="none">
          <polyline points="0.75,44 0.75,0.75 232,0.75"/>
          <polyline points="53,49.25 286.25,49.25 286.25,8"/>
        </g>
      </svg>
      <h1>OUR COLLECTIONS</h1>
    </div>

    <section class="collection-tile" style="top:245px">
      <div class="tile-frame"><div class="tile-inner">
        <div class="tile-rule"></div>
        <div class="tile-photo photo-jewelry" role="img" aria-label="Pair of gold flower stud earrings with small crystals"></div>
        <span class="tile-label">jewelry</span>
      </div></div>
    </section>

    <section class="collection-tile" style="top:472px">
      <div class="tile-frame"><div class="tile-inner">
        <div class="tile-rule"></div>
        <div class="tile-photo photo-home" role="img" aria-label="Round leopard print serving tray"></div>
        <span class="tile-label">The Home</span>
      </div></div>
    </section>

    <section class="collection-tile" style="top:699px">
      <div class="tile-frame"><div class="tile-inner">
        <div class="tile-rule"></div>
        <div class="tile-photo photo-sleep" role="img" aria-label="Lilac velvet slippers with blush pom poms"></div>
        <span class="tile-label">Sleep</span>
      </div></div>
    </section>

    <section class="collection-tile" style="top:926px">
      <div class="tile-frame"><div class="tile-inner">
        <div class="tile-rule"></div>
        <div class="tile-photo photo-accessories" role="img" aria-label="Blush leather tote bag with a teal snake graphic"></div>
        <span class="tile-label">Accessories</span>
      </div></div>
    </section>

    <footer class="footer">
      <span class="footer-item">
        <svg width="16" height="16" viewBox="0 0 16 16" aria-hidden="true">
          <g fill="none" stroke="#2f3233" stroke-width="1.4">
            <circle cx="8" cy="8" r="7"/>
            <ellipse cx="8" cy="8" rx="3" ry="7"/>
            <line x1="1" y1="8" x2="15" y2="8"/>
            <line x1="2.2" y1="4.5" x2="13.8" y2="4.5"/>
            <line x1="2.2" y1="11.5" x2="13.8" y2="11.5"/>
          </g>
        </svg>
        www.verikamode.com
      </span>
      <span class="footer-item">
        <span class="social-dot" aria-hidden="true"></span>
        @verikamode
      </span>
    </footer>
  </main>
</body>
</html>
```